New Organic Skin Care Line Needs to Design a Product Label

***THE WINNER OF THIS PROJECT WILL MOST LIKELY BECOME THE EXCLUSIVE DESIGNER FOR OUR OTHER PRODUCT LABELS***

We need a label design for a new organic skin care product line called "Maple Dune Festoon." This specific product is a 100% pure organic coconut oil. It's used for skin hydration, protection, and makeup removal.

Info to include on front label:

1. Logo: Maple Dune Festoon (attached)
2. Product Name: Pure Coconut Oil (emphasize "organic" somewhere)
3. Slogan: Hydrate your skin and hair.
4. Size: 8 FL OZ 236mL

Attached is:

1. The brand logo "Maple Dune Festoon" with a white background.
2. An image of the bottle we will use.
3. An image of the bottle with lines to show the size and placement of the label.
4. The brand logo "Maple Dune Festoon" with a black background. (photoshop file)

What we need:

A simple mock up of the front side of the label on the bottle. We first want to know what it will look like on the bottle given the size and dimensions.

- We would like one label with a white background (including the logo with a white background).
- We would like a second label with a black background (including the logo with a black background, just need to make the black font white instead of black).

We can get a great idea of what to expect from the front side of the label so we will complete the back side once we identify a winner.
Updates

Apologies, but we are now using a different bottle. The previous one is now discontinued. Please view the two most recent images uploaded. One is an image of the new bottle by itself. The other is an image of that bottle with instructions. Please use your most recent designs on the new bottle. Feel free to make any modifications you see fit to compliment the new bottle shape. Added Friday, March 18, 2016

Project Deadline Extended
Reason: We are still working with the label company to finalize the size. Once the size is confirmed we will have to tweak labels based on finalized measurements.

Target Market(s)

Women, 18-70

Industry/Entity Type

Skin Care Product

Font styles to use
Decorative
Script

Requirements
Must have
• -"shabby sheek" and "cute" theme
• -soft organic feel
• -the ingredients are organic, pure, and natural. That should be an essence of the label.

```html
<!DOCTYPE html>
<html lang="en">
<head>
<meta charset="UTF-8">
<title>Pure Coconut Oil – Label</title>
<link href="https://fonts.googleapis.com/css2?family=Kaushan+Script&family=Caveat:wght@500&family=Cormorant+Garamond:wght@500;600&display=swap" rel="stylesheet">
<style>
  :root {
    --canvas: #ffffff;
    --ring-green: #6e9134;
    --banner-green: #6f9a3a;
    --title-maroon: #551a1e;
    --slogan-ink: #4d3a30;
    --brand-ink: #8a7f7a;
    --size-ink: #3b2f2a;
    --coconut-brown: #7a4a2a;
    --coconut-cream: #f1ebe0;
    --palm-green: #5f7f3a;
    --leaf-faint: #f1f3ee;
  }
  * { margin: 0; padding: 0; box-sizing: border-box; }
  html, body {
    width: 1200px;
    height: 800px;
    overflow: hidden;
    background: var(--canvas);
  }
  .canvas {
    position: relative;
    width: 1200px;
    height: 800px;
  }
  .label {
    position: absolute;
    left: 280px;
    top: 80px;
    width: 640px;
    height: 640px;
  }
  .label-rings {
    position: absolute;
    inset: 0;
  }
  .palm-backdrop {
    position: absolute;
    left: 60px;
    top: 350px;
    width: 340px;
    height: 220px;
    border-radius: 60% 40% 55% 45% / 55% 45% 55% 45%;
    background: linear-gradient(150deg, var(--leaf-faint) 0%, rgba(241,243,238,0.6) 60%, rgba(241,243,238,0) 100%);
  }
  .coconut-art {
    position: absolute;
    left: 250px;
    top: 62px;
    width: 190px;
    height: 150px;
    border-radius: 46% 54% 40% 48% / 52% 48% 52% 48%;
    background: linear-gradient(120deg, var(--palm-green) 0%, var(--coconut-brown) 35%, var(--coconut-brown) 60%, var(--coconut-cream) 85%);
  }
  .organic-banner {
    position: absolute;
    left: 168px;
    top: 82px;
    width: 150px;
    height: 48px;
    background: var(--banner-green);
    border-radius: 6px 20px 6px 16px;
    transform: rotate(-9deg);
    display: flex;
    align-items: center;
    justify-content: center;
  }
  .organic-word {
    font-family: "Kaushan Script", cursive;
    font-size: 28px;
    color: #ffffff;
    line-height: 1;
  }
  .product-name {
    position: absolute;
    left: 0;
    right: 0;
    top: 250px;
    text-align: center;
    font-family: "Kaushan Script", cursive;
    font-size: 72px;
    font-weight: 400;
    color: var(--title-maroon);
    line-height: 1.1;
  }
  .slogan {
    position: absolute;
    left: 0;
    right: 0;
    top: 348px;
    text-align: center;
    font-family: "Caveat", cursive;
    font-size: 38px;
    color: var(--slogan-ink);
    line-height: 1.2;
  }
  .brand-name {
    position: absolute;
    left: 0;
    right: 0;
    top: 488px;
    text-align: center;
    font-family: "Cormorant Garamond", serif;
    font-size: 15px;
    font-weight: 500;
    letter-spacing: 3px;
    text-transform: uppercase;
    color: var(--brand-ink);
  }
  .net-size {
    position: absolute;
    left: 0;
    right: 0;
    top: 524px;
    text-align: center;
    font-family: "Cormorant Garamond", serif;
    font-size: 30px;
    font-weight: 600;
    color: var(--size-ink);
  }
</style>
</head>
<body>
<main class="canvas">
  <section class="label">
    <svg class="label-rings" viewBox="0 0 640 640" aria-hidden="true">
      <ellipse cx="320" cy="322" rx="304" ry="298" fill="none" stroke="var(--ring-green)" stroke-width="4"/>
      <ellipse cx="326" cy="316" rx="290" ry="302" fill="none" stroke="var(--ring-green)" stroke-width="3" transform="rotate(-6 320 320)"/>
    </svg>
    <div class="palm-backdrop" role="img" aria-label="Faint palm leaf decoration"></div>
    <div class="coconut-art" role="img" aria-label="Illustration of a halved coconut with palm leaves"></div>
    <div class="organic-banner"><span class="organic-word">Organic</span></div>
    <h1 class="product-name">Pure Coconut Oil</h1>
    <p class="slogan">Hydrate your skin and hair.</p>
    <p class="brand-name">Maple Dune Festoon</p>
    <p class="net-size">8 FL OZ 236mL</p>
  </section>
</main>
</body>
</html>
```